Mobile Tutoring Service needs a Flier for Distribution to Clients

Lantern Scholars Inc. is a tutoring company that uses video call technology to perform tutoring session in math, sciences, and standardized test preparation. We need a flier that we can distribute to email lists of parents in school districts around the St. Louis Area, as well as post in public areas to attract clients. The following file has the important information needed on the flier. In particular, the "How it Works" Steps 1-3 can be made into an animation or video that looks attractive and helps potential clients understand our process. Our logo is also found in the document. Ideally, all information in the power point slide will be in the flier.

Target Market(s)

Parents for middle and high schoolers grade 6-12 in the St. Louis Area

Industry/Entity Type

Tutoring

Font styles to use
Serif

Colors
3176b5
85abd2
0492cd
33a6d7
ceeaf5

Requirements
Must have
• All the information with the attached file
Nice to have
• A nice-looking animation instead of the still screen shoots that are included in the attached file.

```html
<!DOCTYPE html>
<html lang="en">
<head>
<meta charset="utf-8">
<title>Lantern Scholars – Mobile Tutoring Flier</title>
<link href="https://fonts.googleapis.com/css2?family=Roboto+Condensed:wght@300;400;700&display=swap" rel="stylesheet">
<style>
  :root {
    --page-bg: #1f5d8f;
    --paper: #ffffff;
    --brand-blue: #3f7fc4;
    --band-blue: #4f8ed0;
    --ink: #111111;
    --ink-soft: #1a1a1a;
    --plate-grey: #555555;
    --on-dark: #ffffff;
    --photo-dark: #2a2f36;
    --photo-light: #d9c2b2;
  }
  * { margin: 0; padding: 0; box-sizing: border-box; }
  html, body { width: 1200px; height: 1200px; overflow: hidden; }
  body {
    background: var(--page-bg);
    font-family: "Roboto Condensed", "Arial Narrow", sans-serif;
    position: relative;
  }
  .flier {
    position: absolute; left: 160px; top: 25px;
    width: 880px; height: 1150px;
    background: var(--paper);
    overflow: hidden;
  }
  .flier-shapes { position: absolute; inset: 0; }
  .brand {
    position: absolute; left: 46px; top: 120px; width: 210px;
    text-align: center;
  }
  .brand-dot {
    width: 64px; height: 64px; border-radius: 50%;
    background: var(--brand-blue); margin: 0 auto 22px;
  }
  .brand-name { font-weight: 700; font-size: 33px; color: var(--ink); line-height: 1; }
  .headline {
    position: absolute; left: 318px; top: 42px;
    color: var(--brand-blue); font-weight: 700; line-height: 1.13;
  }
  .headline-lead { font-size: 50px; display: block; }
  .headline-key { font-size: 86px; display: block; line-height: 1; margin-top: 2px; }
  .device-photo { position: absolute; left: 88px; top: 320px; width: 350px; height: 585px; }
  .details { position: absolute; left: 474px; top: 276px; width: 390px; color: var(--on-dark); }
  .detail { margin-bottom: 18px; }
  .detail-title { font-weight: 700; font-size: 24px; color: var(--ink); line-height: 1.1; }
  .detail-text { font-weight: 300; font-size: 21px; line-height: 1.25; }
  .detail-text b { font-weight: 700; }
  .plans-plate { position: absolute; left: 462px; top: 598px; }
  .plans-title {
    position: absolute; left: 474px; top: 600px;
    font-weight: 700; font-size: 36px; color: var(--on-dark); line-height: 44px;
  }
  .plans { position: absolute; left: 474px; top: 654px; width: 380px; color: var(--on-dark); }
  .plan-title { font-weight: 700; font-size: 24px; color: var(--ink); }
  .plan-text { font-weight: 300; font-size: 21px; line-height: 1.25; }
  .plan-text b { font-weight: 700; }
  .plan-sub { position: absolute; left: 474px; top: 750px; font-weight: 700; font-size: 24px; color: var(--ink); }
  .price-tag { position: absolute; left: 472px; top: 780px; }
  .contact {
    position: absolute; left: 0; top: 922px; width: 880px;
    text-align: center; color: var(--on-dark);
  }
  .contact-lead { font-weight: 700; font-size: 37px; line-height: 1.05; }
  .contact-sub { font-weight: 700; font-size: 30px; line-height: 1.2; }
  .contact-rule { width: 714px; height: 1px; background: #888; margin: 14px auto 12px; }
  .contact-phone { font-weight: 700; font-size: 38px; line-height: 1.1; }
  .contact-web { font-weight: 300; font-size: 22px; margin-top: 4px; }
</style>
</head>
<body>
  <main class="flier">
    <svg class="flier-shapes" width="880" height="1150" viewBox="0 0 880 1150">
      <polygon points="0,358 283,258 880,258 880,800 598,905 0,905" fill="var(--band-blue)"/>
      <polygon points="0,910 600,910 880,812 880,1150 0,1150" fill="var(--ink)"/>
    </svg>

    <div class="brand">
      <div class="brand-dot"></div>
      <div class="brand-name">Lantern Scholars</div>
    </div>

    <h1 class="headline">
      <span class="headline-lead">Personalized Tutoring From</span>
      <span class="headline-lead">STEM Experts Via Your</span>
      <span class="headline-key">MOBILE DEVICE</span>
    </h1>

    <svg class="device-photo" role="img" aria-label="Photo of a hand holding a smartphone showing a tutoring chat with handwritten math problems" width="350" height="585" viewBox="0 0 350 585">
      <defs>
        <linearGradient id="photoTone" x1="0" y1="0" x2="1" y2="1">
          <stop offset="0" stop-color="var(--photo-dark)"/>
          <stop offset="1" stop-color="var(--photo-light)"/>
        </linearGradient>
      </defs>
      <rect width="350" height="585" rx="30" fill="url(#photoTone)"/>
    </svg>

    <section class="details">
      <div class="detail">
        <h2 class="detail-title">SUBJECTS</h2>
        <p class="detail-text">All Math, Science, Standardized Test Prep, and Writing 6th-12th grade.</p>
      </div>
      <div class="detail">
        <h2 class="detail-title">OUR TUTORS ARE LOCAL</h2>
        <p class="detail-text">St. Louis PhD candidates or<br>PhD degree holders in STEM fields.</p>
      </div>
      <div class="detail">
        <h2 class="detail-title">NO SCHEDULING REQUIRED!</h2>
        <p class="detail-text">As soon as you send a message for help,<br>a tutor will respond to set up a study session as soon as possible.</p>
      </div>
    </section>

    <svg class="plans-plate" width="300" height="50" viewBox="0 0 300 50">
      <polygon points="0,0 258,0 298,48 0,48" fill="var(--plate-grey)"/>
      <polyline points="258,0 298,48" stroke="#fff" stroke-width="2" fill="none"/>
    </svg>
    <h2 class="plans-title">PAYMENT PLANS</h2>

    <section class="plans">
      <h3 class="plan-title">PAY-AS-YOU-GO</h3>
      <p class="plan-text"><b>$0.83</b>/ minute. <b>$0</b> up-front<br>before session begins!</p>
    </section>
    <h3 class="plan-sub">UNLIMITED SUBSCRIPTION</h3>

    <svg class="price-tag" width="210" height="90" viewBox="0 0 210 90">
      <polygon points="40,5 186,5 206,45 186,85 40,85" fill="var(--plate-grey)"/>
      <circle cx="45" cy="45" r="41" fill="var(--plate-grey)" stroke="#777" stroke-width="2"/>
      <circle cx="45" cy="45" r="36" fill="none" stroke="#bbb" stroke-width="1" stroke-dasharray="3 3"/>
      <text x="45" y="56" text-anchor="middle" font-family="Roboto Condensed, sans-serif" font-weight="700" font-size="32" fill="#fff">$150</text>
      <text x="98" y="55" font-family="Roboto Condensed, sans-serif" font-weight="400" font-size="24" fill="#fff">Per Month</text>
    </svg>

    <footer class="contact">
      <p class="contact-lead">CONTACT US TODAY</p>
      <p class="contact-sub">TO SET UP FOR YOUR FIRST, FREE TUTORING SESSION</p>
      <div class="contact-rule"></div>
      <p class="contact-phone">Phone : 866-555-0142</p>
      <p class="contact-web">www.lanternscholars.com &nbsp;|&nbsp; tutor@lanternscholars.com</p>
    </footer>
  </main>
</body>
</html>
```